Seaside commercial building needs a design for a prominent sign

we have bought a small commercial building in a small seaside area. The building was in disrepair and we are rebuilding it and will rent to small businesses. We have a tall sign right on the corner of the area and want to design something special for the sign The address is 1014 and we want to incorporate that into the name, or just have that as the name. The area is called Bonnet Shores which we were going to use and call it Heron Corner. Almost all shops, however use Bonnet in their name. Looking for something unique with a sea-related logo. Elegant, yet welcoming.

```html
<!DOCTYPE html>
<html lang="en">
<head>
<meta charset="utf-8">
<title>Heron Corner – Sign Concepts</title>
<link href="https://fonts.googleapis.com/css2?family=Roboto+Slab:wght@800&display=swap" rel="stylesheet">
<style>
  :root {
    --paper: #f7f7f7;
    --ink: #2d2d2d;
    --art: #d9d9d9;
  }
  html, body {
    margin: 0;
    padding: 0;
    width: 1200px;
    height: 675px;
    overflow: hidden;
    background: var(--paper);
  }
  .sign-board {
    display: block;
    width: 1200px;
    height: 675px;
  }
  .ink { fill: var(--ink); }
  .paper { fill: var(--paper); }
  .art-area { fill: var(--art); }
  .sign-text {
    font-family: "Roboto Slab", Georgia, serif;
    font-weight: 800;
    fill: var(--paper);
  }
  .address-number {
    font-family: "Roboto Slab", Georgia, serif;
    font-weight: 800;
    fill: var(--ink);
    font-size: 46px;
    text-anchor: middle;
  }
  .building-name { font-size: 42px; text-anchor: middle; }
  .listing { font-size: 35px; letter-spacing: 0.5px; }
</style>
</head>
<body>
<svg class="sign-board" viewBox="0 0 1920 1080" xmlns="http://www.w3.org/2000/svg">
  <defs>
    <g id="frame">
      <rect class="ink" x="168" y="215" width="28" height="713"/>
      <rect class="ink" x="566" y="215" width="28" height="713"/>
      <rect class="ink" x="155" y="203" width="54" height="40" rx="20"/>
      <rect class="ink" x="553" y="203" width="54" height="40" rx="20"/>
    </g>
    <g id="listings">
      <rect class="ink" x="196" y="480" width="370" height="52"/>
      <rect class="ink" x="196" y="558" width="370" height="52"/>
      <rect class="ink" x="196" y="637" width="370" height="51"/>
      <rect class="ink" x="196" y="715" width="370" height="51"/>
      <rect class="ink" x="196" y="794" width="370" height="50"/>
      <circle class="paper" cx="218" cy="507" r="9"/>
      <circle class="paper" cx="218" cy="584" r="9"/>
      <circle class="paper" cx="218" cy="662" r="9"/>
      <circle class="paper" cx="218" cy="740" r="9"/>
      <circle class="paper" cx="218" cy="818" r="9"/>
      <text class="sign-text listing" x="244" y="519">OFFICE SPACE</text>
      <text class="sign-text listing" x="244" y="596">FOR LEASE</text>
      <text class="sign-text listing" x="244" y="675">RENTAL ROOMS</text>
      <text class="sign-text listing" x="244" y="752">CAFE FOR RENT</text>
      <text class="sign-text listing" x="244" y="830">SHOPS</text>
    </g>
    <g id="arched-header">
      <path class="ink" d="M196,441 V305 C200,280 225,265 235,262 L227,252 L285,248 C305,215 345,205 382,205 C419,205 459,215 479,248 L537,252 L529,262 C539,265 564,280 566,305 V441 Z"/>
      <rect class="ink" x="196" y="446" width="370" height="10"/>
      <ellipse class="paper" cx="382" cy="262" rx="82" ry="40"/>
    </g>
  </defs>

  <!-- Concept one: plaque header -->
  <g class="sign sign-plaque">
    <use href="#frame"/>
    <path class="ink" d="M290,245 C300,215 340,208 382,208 C424,208 464,215 474,245 L506,250 L540,254 L534,276 L560,290 C580,330 575,360 565,382 L538,394 L542,412 L506,416 L474,420 C464,450 424,460 382,460 C340,460 300,450 290,420 L258,416 L222,412 L226,394 L199,382 C189,360 184,330 204,290 L230,276 L224,254 L258,250 Z"/>
    <ellipse class="paper" cx="382" cy="250" rx="65" ry="36"/>
    <text class="address-number" x="382" y="267">1014</text>
    <text class="sign-text building-name" x="382" y="352">HERON CORNER</text>
    <rect class="art-area" x="332" y="366" width="108" height="88" rx="40" role="img" aria-label="Anchor illustration"/>
    <use href="#listings"/>
  </g>

  <!-- Concept two: arched header with waves -->
  <g class="sign sign-waves" transform="translate(595,0)">
    <use href="#frame"/>
    <use href="#arched-header"/>
    <text class="address-number" x="382" y="279">1014</text>
    <text class="sign-text building-name" x="382" y="347">HERON CORNER</text>
    <rect class="art-area" x="265" y="362" width="240" height="64" rx="24" role="img" aria-label="Curling sea waves illustration"/>
    <use href="#listings"/>
  </g>

  <!-- Concept three: arched header with wave and sun -->
  <g class="sign sign-sunwave" transform="translate(1175,0)">
    <use href="#frame"/>
    <use href="#arched-header"/>
    <text class="address-number" x="382" y="279">1014</text>
    <text class="sign-text building-name" x="382" y="347">HERON CORNER</text>
    <rect class="art-area" x="303" y="360" width="154" height="66" rx="28" role="img" aria-label="Wave and setting sun illustration"/>
    <use href="#listings"/>
  </g>
</svg>
</body>
</html>
```